Computer Repair Business - Needs New Business Card Design

I want to create a very cool business card for my business. I want to make it 100% different from my previous card. I would like to use similar color scheme like Royal blue.

With this card I want to create a conversation and have my customers say "Wow, that's a cool business card" Trying to prevent it from looking like the typical card that get's shoved into a wallet.

My website is below:

www.milospcworks.com

I want to edit the hours and website and email:

www.milospcworks.com
milo@milospcworks.com

10:30 to 6pm Monday - Friday
10:30 to 3pm Saturday

Just to remind, when i see a new design i don't want to notice my old design.

Business card will be printed and made with rounded corners and horizontal.

The back of the card should say " In-Store Repair, Remote Support, Data Recovery"

Industry/Entity Type

Business

Font styles to use
Sans Serif

Colors
33a6d7
3176b5

Requirements
Must have
• Clean looking - have creative aspects.
Should not have
• Should not look like the previous card design.

```html
<!DOCTYPE html>
<html lang="en">
<head>
<meta charset="utf-8">
<title>Milo's PC Works – Business Card</title>
<link href="https://fonts.googleapis.com/css2?family=Open+Sans:ital,wght@0,400;0,600;0,700;1,600&display=swap" rel="stylesheet">
<style>
  :root {
    --royal: #1f63b4;
    --royal-deep: #174f94;
    --sky: #33a6d7;
    --mid-blue: #3176b5;
    --ink: #2a2f36;
    --muted: #5b6470;
    --paper: #ffffff;
    --paper-shade: #e9ecef;
    --stage: #eef1f4;
  }
  * { box-sizing: border-box; margin: 0; padding: 0; }
  html, body {
    width: 1200px; height: 899px; overflow: hidden;
    background: var(--stage);
    font-family: "Open Sans", Arial, sans-serif;
  }
  .canvas {
    width: 1200px; height: 899px;
    display: flex; align-items: center; justify-content: center; gap: 40px;
  }
  .card {
    position: relative;
    width: 540px; height: 309px;
    border-radius: 26px;
    overflow: hidden;
    box-shadow: 0 12px 30px rgba(20, 40, 70, .18);
  }

  /* Front */
  .card--front {
    background: linear-gradient(135deg, var(--paper) 0%, var(--paper) 55%, var(--paper-shade) 100%);
    color: var(--ink);
  }
  .brand {
    position: absolute; left: 40px; top: 86px;
    width: 210px;
    display: flex; align-items: center; gap: 12px;
  }
  .brand__mark {
    width: 30px; height: 30px; background: var(--royal); flex: none;
  }
  .brand__name {
    font-size: 23px; font-weight: 600; letter-spacing: .5px;
    color: var(--royal);
    line-height: 1.1;
  }
  .person {
    position: absolute; left: 282px; top: 44px;
  }
  .person__name {
    font-size: 17px; font-weight: 600; letter-spacing: .8px;
    color: var(--royal); text-transform: uppercase;
  }
  .person__role { font-size: 12.5px; color: var(--ink); margin-top: 1px; }
  .address {
    position: absolute; left: 282px; top: 118px;
    font-size: 14.5px; line-height: 1.45; color: var(--ink);
  }
  .contacts {
    position: absolute; left: 282px; top: 186px;
    list-style: none; font-size: 10.5px; color: var(--muted);
  }
  .contacts li { display: flex; align-items: center; gap: 7px; height: 15px; }
  .contacts svg { width: 10px; height: 10px; fill: var(--royal); flex: none; }
  .swoosh { position: absolute; left: 0; bottom: 0; width: 540px; height: 96px; }
  .front-url {
    position: absolute; left: 142px; bottom: 24px;
    font-size: 12px; font-style: italic; font-weight: 600;
    color: var(--paper); letter-spacing: .3px;
  }

  /* Back */
  .card--back {
    background: linear-gradient(160deg, var(--mid-blue) 0%, var(--royal) 50%, var(--royal-deep) 100%);
    color: var(--paper);
  }
  .services {
    position: absolute; left: 0; right: 0; top: 54px;
    display: flex; justify-content: space-around; padding: 0 26px;
    list-style: none;
  }
  .service {
    width: 140px; text-align: center;
    display: flex; flex-direction: column; align-items: center; gap: 12px;
  }
  .service svg { width: 52px; height: 52px; }
  .service__label { font-size: 14px; font-weight: 600; line-height: 1.25; }
  .hours {
    position: absolute; left: 0; right: 0; bottom: 44px;
    text-align: center; font-size: 11.5px; line-height: 1.6;
    color: rgba(255, 255, 255, .9);
  }
  .hours__rule {
    position: absolute; left: 60px; right: 60px; bottom: 96px;
    height: 1px; background: rgba(255, 255, 255, .35);
  }
</style>
</head>
<body>
<main class="canvas">

  <section class="card card--front" aria-label="Business card front">
    <div class="brand">
      <span class="brand__mark"></span>
      <span class="brand__name">MILO'S<br>PC WORKS</span>
    </div>

    <div class="person">
      <p class="person__name">Owen Hartley</p>
      <p class="person__role">Managing Director</p>
    </div>

    <p class="address">127 Larkspur Ave,<br>Fairview, NJ 07014</p>

    <ul class="contacts">
      <li>
        <svg viewBox="0 0 24 24"><path d="M6.6 10.8a15.1 15.1 0 0 0 6.6 6.6l2.2-2.2a1 1 0 0 1 1-.25 11.4 11.4 0 0 0 3.6.57 1 1 0 0 1 1 1V20a1 1 0 0 1-1 1A17 17 0 0 1 3 4a1 1 0 0 1 1-1h3.5a1 1 0 0 1 1 1c0 1.25.2 2.45.57 3.57a1 1 0 0 1-.25 1z"/></svg>
        555.014.2087
      </li>
      <li>
        <svg viewBox="0 0 24 24"><path d="M2 5h20v14H2zm2 2v.5l8 5 8-5V7z"/></svg>
        milo@milospcworks.com
      </li>
      <li>
        <svg viewBox="0 0 24 24"><path d="M12 2a10 10 0 1 0 0 20 10 10 0 0 0 0-20zm6.9 6h-3a15 15 0 0 0-1.3-3.9A8 8 0 0 1 18.9 8zM12 4c.8 1.2 1.5 2.5 1.9 4h-3.8c.4-1.5 1.1-2.8 1.9-4zM4.3 14a8 8 0 0 1 0-4h3.4a16 16 0 0 0 0 4zm.8 2h3a15 15 0 0 0 1.3 3.9A8 8 0 0 1 5.1 16zm3-8h-3a8 8 0 0 1 4.3-3.9A15 15 0 0 0 8.1 8zM12 20c-.8-1.2-1.5-2.5-1.9-4h3.8c-.4 1.5-1.1 2.8-1.9 4zm2.3-6H9.7a14 14 0 0 1 0-4h4.6a14 14 0 0 1 0 4zm.3 5.9a15 15 0 0 0 1.3-3.9h3a8 8 0 0 1-4.3 3.9zm1.7-5.9a16 16 0 0 0 0-4h3.4a8 8 0 0 1 0 4z"/></svg>
        www.milospcworks.com
      </li>
    </ul>

    <svg class="swoosh" viewBox="0 0 540 96" preserveAspectRatio="none" aria-hidden="true">
      <path d="M0 28 C150 42 360 62 540 96 L0 96 Z" fill="var(--sky)"/>
      <path d="M0 38 C160 50 360 70 520 96 L0 96 Z" fill="var(--royal)"/>
      <path d="M0 30 C160 40 340 58 470 96" fill="none" stroke="var(--ink)" stroke-width="1.2" opacity=".55"/>
    </svg>
    <p class="front-url">www.milospcworks.com</p>
  </section>

  <section class="card card--back" aria-label="Business card back">
    <ul class="services">
      <li class="service">
        <svg viewBox="0 0 52 52" fill="none" stroke="var(--paper)" stroke-width="2.4" stroke-linecap="round" stroke-linejoin="round">
          <path d="M33 8a9 9 0 0 0-8.5 12L10 34.5a3.5 3.5 0 0 0 5 5L29.5 25A9 9 0 0 0 41.5 16l-5.5 5.5-5-1-1-5L35.5 10A9 9 0 0 0 33 8z"/>
        </svg>
        <span class="service__label">In-Store Repair</span>
      </li>
      <li class="service">
        <svg viewBox="0 0 52 52" fill="none" stroke="var(--paper)" stroke-width="2.4" stroke-linecap="round" stroke-linejoin="round">
          <path d="M11 28v-4a15 15 0 0 1 30 0v4"/>
          <rect x="8" y="27" width="7" height="12" rx="2"/>
          <rect x="37" y="27" width="7" height="12" rx="2"/>
          <path d="M41 39c0 4-4 6-10 6h-3"/>
        </svg>
        <span class="service__label">Remote Support</span>
      </li>
      <li class="service">
        <svg viewBox="0 0 52 52" fill="none" stroke="var(--paper)" stroke-width="2.4" stroke-linecap="round" stroke-linejoin="round">
          <rect x="14" y="14" width="24" height="24" rx="2"/>
          <rect x="20" y="20" width="12" height="12" fill="var(--paper)"/>
          <path d="M20 8v6M26 8v6M32 8v6M20 38v6M26 38v6M32 38v6M8 20h6M8 26h6M8 32h6M38 20h6M38 26h6M38 32h6"/>
        </svg>
        <span class="service__label">Data Recovery</span>
      </li>
    </ul>

    <div class="hours__rule"></div>
    <p class="hours">
      MON – FRI 10:30 am – 6:00 pm / SAT 10:30 am – 3:00 pm<br>
      Sunday by appointment
    </p>
  </section>

</main>
</body>
</html>
```